energy rating company

Web Design graphics and layout only

To create two pages for the website. First the home page and the second is the design for the job board for our clients use after login. I have attached files that explain in detail what the pages should have and the purpose/desires of each object. Please read these thoroughly.

The webpages need to be clean, professional, easy on the eye, obvious in all its buttons and functions with a strong call to action on the home page and branding and clean, great and obvious looking buttons and very simple but dynamic as well. We wish to be seen as contemporary.

Business Concept

Our business concept is simple, to build a website whereby our clients will be able to upload jobs for energy raters to quote on and subsequent complete the work if their quote is selected. To link energy ratings that are required with energy raters via our website. Similarly to the varn website, jobs will be “advertised” on the job board and raters will select which jobs they wish to quote for.

I have attached a Word document explaining all the parts of the website and another word document showing what we are sort of after and a excel spreadsheet as well. Please read these in conjunction with this brief!
Updates

Dear All

I have submitted with my brief a word doc and excel spreadsheet of the two pages I want created.  However this is not the layout or design I want, I only put it together so that you will need to know what is required on each page.  Feel free to change and redesign it all.

Also the second page does not require the "process" logo or any other menu items except the first five being Home, How it works, About Us, testimonials and Contact us as per the home page.

We also are looking for something very professional and very clean.  It should be very easy to see exactly what you are looking for.

I will also extend the deadline for new designers!!  I am excited to see your talents!!

Thanks

I have increase budget and posted a note saying feel free to change all the details layout etc on my brief just include everything!!! 

Wanting a professional corporate look...

Want a professional corporate look

We have changed our minds and you we no longer require the process to be on the home page.

Thanks

Target Market(s)

Target Market

Home Inspection Companies
Pest Inspection Companies
Residential home buyers/sellers
Real Estate companies

Industry/Entity Type

It Company

Number of Pages Required

1 page

Requirements
Must have
• Colours and Styles

• The website should be mainly white as I believe it is seen as clean and simple with colour from the logos, but can be swayed if it projects the image we are after.

• It should be obvious and process orientated and I do believe symbols, pictures, etc should replace words where possible.

```html
<!DOCTYPE html>
<html lang="en">
<head>
<meta charset="utf-8">
<title>Ratewell Australia – Energy Rating Quotes</title>
<link href="https://fonts.googleapis.com/css2?family=Source+Sans+3:wght@400;600&family=Arimo:wght@400;700&family=Lora:ital,wght@0,400;1,400;1,700&display=swap" rel="stylesheet">
<style>
:root{
  --green-top:#62b23a;
  --green-bottom:#1f9547;
  --nav-green:#1d7a3c;
  --orange-top:#e8b233;
  --orange-bottom:#c9761a;
  --brand-orange:#c0561a;
  --brand-green:#2f8f3b;
  --lead-green:#5aa829;
  --callout-text:#e4960c;
  --text:#444;
  --muted:#9a9a9a;
  --tick:#3aa53c;
  --login-top:#5f9f34;
  --login-bottom:#a6c22f;
  --quote-green:#9cc13a;
  --photo-frame:#f2a51a;
  --footer-text:#9be58b;
}
*{margin:0;padding:0;box-sizing:border-box}
html,body{width:1200px;height:1168px;overflow:hidden}
body{
  position:relative;
  background:linear-gradient(180deg,var(--green-top) 0%,#3aa03d 45%,var(--green-bottom) 100%);
  font-family:"Arimo",Arial,sans-serif;color:var(--text);
}
.page{position:absolute;left:74px;top:33px;width:1054px;height:1069px;background:#fff;border-radius:10px;box-shadow:0 2px 6px rgba(0,0,0,.25)}
.brand{position:absolute;left:69px;top:40px;width:364px;height:137px;background:linear-gradient(180deg,#fff,#f0f0f0);border-radius:4px;box-shadow:0 2px 5px rgba(0,0,0,.3);display:flex;align-items:center;gap:18px;padding-left:28px}
.brand-dot{width:72px;height:72px;border-radius:50%;background:#e0a020;flex:none}
.brand-name{font-family:"Source Sans 3",sans-serif;font-weight:600;font-size:34px;line-height:1.05;color:var(--brand-orange)}
.main-nav{position:absolute;left:451px;top:31px;width:656px;height:53px;background:var(--nav-green);border-radius:0 0 8px 8px;display:flex;align-items:center;font-family:"Source Sans 3",sans-serif;font-size:19px;color:#fff}
.main-nav a{color:#fff;text-decoration:none;padding:0 10px;height:100%;display:flex;align-items:center}
.main-nav a.current{background:#176832;padding:0 14px}
.cta{position:absolute;top:104px;width:205px;height:69px;border-radius:7px;background:linear-gradient(180deg,var(--orange-top) 0%,#dc9a28 50%,#d18420 51%,var(--orange-bottom) 100%);color:#fff;font-family:"Source Sans 3",sans-serif;text-align:center;display:flex;flex-direction:column;justify-content:center;line-height:1.05;box-shadow:0 1px 3px rgba(0,0,0,.25)}
.cta strong{font-weight:400;font-size:25px}
.cta small{font-size:16px}
.process{position:absolute;left:95px;top:204px;width:1009px;height:141px;border-radius:10px;background:linear-gradient(180deg,#f2f2f2,#fff 50%,#f4f4f4);display:flex;align-items:center;justify-content:space-around;font-family:"Source Sans 3",sans-serif;font-size:21px;color:#666;text-align:center;line-height:1}
.process .step{width:150px}
.process b{font-weight:400;color:#222}
.process svg{width:40px;height:56px}
.lead{position:absolute;left:104px;top:368px;width:650px;font-size:18.5px;line-height:26px;color:var(--lead-green);font-weight:700}
.about{position:absolute;left:104px;top:464px;width:650px;font-size:16px;line-height:22px;color:#555}
.callout{position:absolute;left:70px;top:528px;width:702px;height:157px;background:linear-gradient(180deg,#fff 0%,#fdf4e0 60%,#fde3b0 100%);border-radius:6px;box-shadow:0 1px 4px rgba(0,0,0,.25);padding:22px 34px;color:var(--callout-text)}
.callout p{font-size:22px;line-height:32px}
.callout p.big{font-size:27px;margin-top:14px}
.decor{position:absolute;left:74px;top:740px;width:470px;height:360px;background:radial-gradient(circle at 65% 100%,rgba(230,200,160,.35),rgba(200,225,140,.2) 45%,rgba(255,255,255,0) 70%)}
.register{position:absolute;left:104px;top:703px;width:660px;font-size:16.5px;line-height:22px;color:var(--muted);font-weight:700}
.benefits{position:absolute;left:120px;top:782px;list-style:none;font-size:16.5px;line-height:22px;color:#444}
.benefits li{display:flex;align-items:center;gap:8px}
.benefits svg{width:14px;height:14px}
.free-note{position:absolute;left:104px;top:955px;width:640px;font-size:16.5px;line-height:22px;font-weight:700;color:#333}
.login{position:absolute;left:791px;top:368px;width:341px;height:202px;background:linear-gradient(180deg,var(--login-top),var(--login-bottom));box-shadow:0 2px 5px rgba(0,0,0,.3);border-radius:6px 0 6px 6px;padding:14px 22px 0 22px;color:#111}
.login label{display:flex;align-items:center;gap:8px;font-family:"Source Sans 3",sans-serif;font-size:21px}
.login label::before{content:"";width:9px;height:9px;border-radius:50%;background:#1c5d25;box-shadow:0 0 0 2px #c8e68a}
.field{height:35px;border-radius:7px;background:#fff;margin:6px 0 14px;font-size:17px;color:#777;padding:7px 10px;box-shadow:inset 0 2px 3px rgba(0,0,0,.15)}
.forgot{font-size:12.5px;color:#fff;margin-top:-4px}
.testimonials{position:absolute;left:804px;top:607px;width:302px;height:427px;border-radius:8px;background:linear-gradient(180deg,#f2f2f2 0,#fff 60px,#fff 380px,#f2f2f2 100%)}
.testimonials h2{font-family:"Source Sans 3",sans-serif;font-weight:400;font-size:29px;color:var(--brand-green);margin:14px 0 0 0;letter-spacing:.3px}
.quote{position:absolute;left:0;width:302px;font-family:"Lora",serif}
.quote .text{position:absolute;left:34px;width:150px;text-align:right;font-size:14.5px;line-height:19.7px;color:#999}
.quote .photo{position:absolute;left:196px;width:88px;height:88px;border:2px solid var(--photo-frame)}
.quote .mark{position:absolute;font-size:46px;line-height:1;color:var(--quote-green);font-weight:700}
.quote .who{position:absolute;left:5px;font-style:italic}
.quote .who b{display:block;font-size:14.5px;color:#333}
.quote .who span{font-size:12px;color:#333}
.copyright{position:absolute;left:74px;top:1113px;font-size:12.5px;color:var(--footer-text)}
</style>
</head>
<body>
<div class="page"></div>

<div class="brand">
  <span class="brand-dot"></span>
  <span class="brand-name">Ratewell<br>Australia</span>
</div>

<nav class="main-nav">
  <a class="current" href="#">HOME</a>
  <a href="#">HOW IT WORKS?</a>
  <a href="#">FAQ's</a>
  <a href="#">ABOUT US</a>
  <a href="#">TESTIMONIALS</a>
  <a href="#">CONTACT US</a>
</nav>

<a class="cta" style="left:459px"><strong>GET QUOTES</strong></a>
<a class="cta" style="left:677px"><strong>ENERGY RATERS</strong><small>Add your business</small></a>
<a class="cta" style="left:894px"><strong>ACTIVE<br>JOB BOARD</strong></a>

<section class="process">
  <div class="step"><b>Post a job</b></div>
  <svg viewBox="0 0 40 56"><path d="M6 4 L32 28 L6 52" fill="none" stroke="#2a9a4a" stroke-width="10"/></svg>
  <div class="step">Get as many quotes as <b>you like</b></div>
  <svg viewBox="0 0 40 56"><path d="M6 4 L32 28 L6 52" fill="none" stroke="#2a9a4a" stroke-width="10"/></svg>
  <div class="step">Select energy quote that <b>suits</b></div>
  <svg viewBox="0 0 40 56"><path d="M6 4 L32 28 L6 52" fill="none" stroke="#2a9a4a" stroke-width="10"/></svg>
  <div class="step">Approve <b>payment</b></div>
  <svg viewBox="0 0 40 56"><path d="M6 4 L32 28 L6 52" fill="none" stroke="#2a9a4a" stroke-width="10"/></svg>
  <div class="step">Receive <b>Rating</b></div>
</section>

<p class="lead">We provide you with solutions to your energy rating needs!&nbsp; Get up to 10 competitive quotes for your energy ratings from our database of professional accredited energy raters in all states and territories!</p>
<p class="about">Ratewell australia is Australia's leading professional energy rating consultancy firm specializing in large scaled residential and commercial energy rating logistics.</p>

<div class="callout">
  <p>It's Free, Fast and Easy to use and you get the best price and turnaround time that suits you!!</p>
  <p class="big">Its a one stop shop for your energy rating needs!!</p>
</div>

<div class="decor" role="img" aria-label="Faint decorative dashed arcs in green and tan"></div>

<p class="register">Register with us, upload your job and specifications, and sit back and watch as energy raters provide quotes for your work!</p>

<ul class="benefits">
  <li><svg viewBox="0 0 14 14"><path d="M1 7 L5 11 L13 2" fill="none" stroke="#3aa53c" stroke-width="3"/></svg>Get up to 10 best priced quotes for your energy ratings</li>
  <li><svg viewBox="0 0 14 14"><path d="M1 7 L5 11 L13 2" fill="none" stroke="#3aa53c" stroke-width="3"/></svg>You save time</li>
  <li><svg viewBox="0 0 14 14"><path d="M1 7 L5 11 L13 2" fill="none" stroke="#3aa53c" stroke-width="3"/></svg>Be able to specify your desired turnaround times</li>
  <li><svg viewBox="0 0 14 14"><path d="M1 7 L5 11 L13 2" fill="none" stroke="#3aa53c" stroke-width="3"/></svg>You can upload a job for quoting anytime and anywhere</li>
  <li><svg viewBox="0 0 14 14"><path d="M1 7 L5 11 L13 2" fill="none" stroke="#3aa53c" stroke-width="3"/></svg>Choose a deadline for energy raters to supply quotes</li>
  <li><svg viewBox="0 0 14 14"><path d="M1 7 L5 11 L13 2" fill="none" stroke="#3aa53c" stroke-width="3"/></svg>Be able to track your numerous jobs in one place</li>
</ul>

<p class="free-note">Its totally free to be registered with us and there is no obligations or hidden catches!</p>

<form class="login">
  <label>User</label>
  <div class="field">mikaelren</div>
  <label>Password</label>
  <div class="field">●●●●●●●●●●</div>
  <p class="forgot">Did you forget your password</p>
</form>

<aside class="testimonials">
  <h2>TESTIMONIALS</h2>
  <div class="quote" style="top:57px">
    <span class="mark" style="left:-2px;top:0">“</span>
    <p class="text" style="top:5px">Lorem ipsum dolor sit amet, consectetur adipiscing elit. Phasellus arcu magna, condimentum id consequat quis,</p>
    <div class="photo" style="top:2px;background:linear-gradient(160deg,#6a4a32,#c8906a 55%,#3a2a20)" role="img" aria-label="Portrait photo of a customer"></div>
    <div class="who" style="top:136px"><b>Lena Moravec</b><span>Valletta, Malta</span></div>
    <span class="mark" style="left:262px;top:140px">”</span>
  </div>
  <div class="quote" style="top:259px">
    <span class="mark" style="left:-2px;top:0">“</span>
    <p class="text" style="top:5px">Lorem ipsum dolor sit amet, consectetur adipiscing elit. Phasellus arcu</p>
    <div class="photo" style="top:2px;background:linear-gradient(160deg,#d8d8d8,#8a7a70 55%,#2a2a2a)" role="img" aria-label="Portrait photo of a customer"></div>
    <div class="who" style="top:115px"><b>Owen Pritchard</b><span>Ohio, United States</span></div>
    <span class="mark" style="left:262px;top:119px">”</span>
  </div>
</aside>

<p class="copyright">Copyright 2010 - Ratewell Australia&nbsp; - All rights reserved</p>
</body>
</html>
```